Yard Waste Graphic

Need to have a graphic showing yard waste that we can post on materials and on our website. A simple graphic showing some 30 gallon biodegradable bags, and a bundle of brush that's no longer than 4 feet in length. I'll attach the guidelines. Like picture but without the carts. Here is more info. https://www.brennockvale.example/gov/departments/pw/spring_yard_collection.asp

```html
<!DOCTYPE html>
<html lang="en">
<head>
<meta charset="utf-8">
<title>Organic Spring Yard Waste</title>
<link href="https://fonts.googleapis.com/css2?family=Jost:wght@400;500&family=Arimo:wght@400&display=swap" rel="stylesheet">
<style>
  :root {
    --navy: #0b3a82;
    --brick: #a8322a;
    --white: #ffffff;
    --ink: #111111;
    --backdrop: #e6e8eb;
    --blossom: #c98fb4;
    --foliage: #5f8f3a;
    --lawn: #7fb046;
  }
  * { margin: 0; padding: 0; box-sizing: border-box; }
  html, body {
    width: 1200px;
    height: 923px;
    overflow: hidden;
    background: var(--backdrop);
  }
  .sheet {
    position: absolute;
    left: 25px;
    top: 116px;
    width: 1045px;
    height: 628px;
    transform: scale(1.1);
    transform-origin: 0 0;
    background: var(--white);
    overflow: hidden;
  }
  .sheet-shapes { position: absolute; inset: 0; }
  .title {
    position: absolute;
    left: 300px;
    right: 0;
    top: 0;
    height: 75px;
    display: flex;
    align-items: center;
    justify-content: center;
    padding-left: 60px;
    font-family: 'Jost', sans-serif;
    font-weight: 400;
    font-size: 57px;
    letter-spacing: -0.5px;
    color: var(--white);
  }
  .section-head {
    position: absolute;
    display: flex;
    align-items: center;
    gap: 10px;
    font-family: 'Jost', sans-serif;
    font-weight: 400;
    font-size: 29px;
    color: var(--navy);
    white-space: nowrap;
  }
  .section-head svg { flex: none; }
  .head-accepted { left: 425px; top: 85px; }
  .head-unaccepted { left: 731px; top: 84px; }
  .head-prepare { left: 527px; top: 306px; color: var(--white); font-size: 31px; }
  .rule-list {
    position: absolute;
    list-style: none;
    font-family: 'Arimo', sans-serif;
    font-size: 14.3px;
    line-height: 19.6px;
    color: var(--ink);
  }
  .rule-list li { padding-left: 8px; text-indent: -8px; }
  .list-accepted { left: 466px; top: 129px; width: 250px; }
  .list-unaccepted { left: 773px; top: 129px; width: 265px; }
  .list-prepare { left: 473px; top: 361px; width: 565px; }
  .list-prepare li { padding-left: 0; text-indent: 0; }
</style>
</head>
<body>
  <main class="sheet">
    <svg class="sheet-shapes" width="1045" height="628" viewBox="0 0 1045 628">
      <defs>
        <linearGradient id="garden-tones" x1="0" y1="0" x2="0" y2="1">
          <stop offset="0" stop-color="#d7a3c6"/>
          <stop offset="0.35" stop-color="var(--blossom)"/>
          <stop offset="0.55" stop-color="var(--foliage)"/>
          <stop offset="0.8" stop-color="var(--lawn)"/>
          <stop offset="1" stop-color="#b9a07a"/>
        </linearGradient>
      </defs>
      <path class="arc-band" d="M300 0 Q570 314 340 628 L1045 628 L1045 0 Z" fill="var(--navy)"/>
      <path class="arc-inner" d="M322 0 Q592 314 362 628 L1045 628 L1045 0 Z" fill="var(--white)"/>
      <rect class="title-band" x="300" y="0" width="745" height="75" fill="var(--navy)"/>
      <rect class="prepare-band" x="450" y="302" width="595" height="48" fill="var(--navy)"/>
      <path class="arc-rule" d="M295 0 Q565 314 335 628" fill="none" stroke="var(--brick)" stroke-width="5"/>
      <path class="garden-photo" role="img" aria-label="Photo of blossoming trees over a lawn with two filled paper yard waste bags and a bundle of twigs and pinecones"
            d="M0 0 L291 0 Q561 314 331 628 L0 628 Z" fill="url(#garden-tones)"/>
    </svg>

    <h1 class="title">Organic Spring Yard Waste</h1>

    <h2 class="section-head head-accepted">
      <svg width="38" height="38" viewBox="0 0 38 38" aria-hidden="true">
        <circle cx="18" cy="20" r="15" fill="none" stroke="var(--navy)" stroke-width="3.5"/>
        <path d="M9 19 L17 28 L35 4" fill="none" stroke="var(--navy)" stroke-width="5" stroke-linecap="round" stroke-linejoin="round"/>
      </svg>
      Accepted Material
    </h2>
    <ul class="rule-list list-accepted">
      <li>- Acorns, Dead plants, Dethatching material .</li>
      <li>- Flower and vegetable bed debris (cornstalks, tomato plants etc.)</li>
      <li>- Leaves, Pine needles, Pinecones, Twigs, Weeds.</li>
      <li>- Grass clippings combined with the above materials.</li>
    </ul>

    <h2 class="section-head head-unaccepted">
      <svg width="38" height="38" viewBox="0 0 38 38" aria-hidden="true">
        <circle cx="18" cy="19" r="15" fill="none" stroke="var(--navy)" stroke-width="3.5"/>
        <path d="M8 8 L29 30 M29 8 L8 30" stroke="var(--navy)" stroke-width="5" stroke-linecap="round"/>
      </svg>
      Unaccepted Material
    </h2>
    <ul class="rule-list list-unaccepted">
      <li>- Yard waste placed in plastic bags, trash cans, cardboard boxes, bundles tied with wire or in other containers.</li>
      <li>- Paper leaf bags containing branches, trash, grass, soil, rocks, bulky or metal tems will not be collected.</li>
      <li>- Bags with grass clippings only can not be collected.</li>
    </ul>

    <h2 class="section-head head-prepare">
      <svg width="40" height="40" viewBox="0 0 40 40" aria-hidden="true">
        <circle cx="20" cy="20" r="18" fill="none" stroke="var(--white)" stroke-width="2.5"/>
        <path d="M20 9 L20 24" stroke="var(--white)" stroke-width="3.5" stroke-linecap="round"/>
        <circle cx="20" cy="30" r="2.2" fill="var(--white)"/>
      </svg>
      How to Prepare for Collection
    </h2>
    <ul class="rule-list list-prepare">
      <li>- Use only yard waste 30 gallon biodegradable paper bags.</li>
      <li>- Grass clippings must be combined with other material. Remove dirt from roots.</li>
      <li>- Do not mix fruits, vegetables, trash, or animal droppings with your yard waste.</li>
      <li>- Do not overload yard waste bags.&nbsp; Bags must weigh less than 40 pounds.</li>
      <li>- Do not use plastic bags or cardboard boxes for yard waste.</li>
      <li>- Dirt and sod are not acceptable as yard waste.</li>
      <li>- No seasonal decoration made with wire frames and plastic materials.</li>
      <li>- Tree limbs, brush, debris must be cut into 4-foot lengths and bundled using biodegradable material and must weigh less than 40 pounds.</li>
      <li>-Yard waste should never be blown or swept into the street</li>
      <li>-Close your bags by folding them down</li>
      <li>-Bundle branches and brush up to 4 inches in diameter and 4 feet in length with organic twine (wire, nylon or plastic twine not allowed)</li>
    </ul>
  </main>
</body>
</html>
```